IT Services company requires a services website design with integrated blog

We at Brambleway Code Haulage primarily provide application migration consultancy (e.g. moving applications from Paneview QR to Paneview 5) and application virtualization (e.g. Dunmore Box-K) consultancy.This process is commonly known as 'packaging' but doesnt involve cardboard boxes ;) (however, I am happy to use that visual analogy if you want to use any box graphics) We also provide application compatibility testing, software auditing and application portfolio management.

We are looking for a complete redesign of our current horrible diy attempt at a website at www.brambleway-example.com. We have had created a rebranded logo (attached files and fonts) and a rebranded business card (also attached) We would like the website to match the same/similar colors and styling as these.

I want to redisgn the website so that the main focus of this website is to show our subject matter expertise with a blog and should take up most of the websites real estate and focus on the home screen. Then if the customer wants, they can use our services to help them in their own application migration/deployment projects by browsing our details in links/buttons somewhere

In any of the designs, please do not include my Velharo or Dunmore partnerships.  Thank you

Target Market(s)

Application packagers / engineers looking for technical articles

Application migration project managers

Industry/Entity Type

Real Estate

Requirements
Must have
• This site is primarily a blog site. The blog should have buttons to share each article on social media site. It should be easy for me to create or edit new blog articles (have technical skills but not creative ones). Each article should also allow for comments (do not require approval but should allow for admin removal) but do not add like/vote buttons because i do not expect large enough traffic and could be determental.

There should be a contact page to host contact information and an email box that goes to enquiries@brambleway-example.com

The other pages should include About us and Services (placeholder text to be used as current site text needs overhauling but original text can be used in the design just remember when placing that the text may shorten or increase etc.)

All text has to be easily editable (no over use of text in images where possible)
Nice to have
• An email notification of new comments to articles sent to webadmin@brambleway-example.com

Newsletter subscription
Should not have
• Do not include vote/like buttons or website counters. Initial traffic is not going to be large enough to warrant these features and may reflect badly on the site.

No logon features. Site content and commenting should be open access

No opinion polls

No why choose us section from current website

Do not include partner information in new site (Velharo and Dunmore)

DO NOT JUST REPLICATE EXISTING WEBSITE FEATURES, PLEASE REFER TO THIS BRIEF. THIS SITE NEEDS TO PRIMARILY BE A BLOG

```html
<!DOCTYPE html>
<html lang="en">
<head>
<meta charset="utf-8">
<title>Brambleway Code Haulage</title>
<link href="https://fonts.googleapis.com/css2?family=Ubuntu:wght@300;400;500&display=swap" rel="stylesheet">
<style>
:root{
  --blue:#7083de;
  --blue-dark:#5367c9;
  --blue-light:#8e9ee8;
  --ink:#444;
  --muted:#a3a3a3;
  --line:#e4e4e4;
  --panel:#f8f8f8;
  --footer:#343434;
}
*{box-sizing:border-box;margin:0;padding:0}
html,body{width:1200px;height:1181px;overflow:hidden}
body{font-family:"Ubuntu",sans-serif;background:#fff;color:var(--ink);position:relative}
.site-header{position:absolute;left:0;top:0;width:1200px;height:86px;background:linear-gradient(#f6f6f6,#fbfbfb)}
.brand{position:absolute;left:171px;top:28px;display:flex;align-items:center;gap:10px}
.brand-dot{width:26px;height:26px;border-radius:50%;background:var(--blue)}
.brand-name{font-size:19px;font-weight:300;color:#8a8a8a}
.main-nav{position:absolute;left:483px;top:0;display:flex;height:86px}
.main-nav a{display:block;line-height:84px;font-size:13px;font-weight:300;color:#888;text-decoration:none;padding:0 13px}
.main-nav a.active{background:var(--blue);color:#fff;width:76px;text-align:center;padding:0;position:relative}
.main-nav a.active::after{content:"";position:absolute;left:0;top:86px;border-top:16px solid var(--blue);border-right:16px solid transparent}
.support{position:absolute;left:852px;top:25px;display:flex;align-items:center;gap:7px}
.support-text{text-align:left}
.support-label{font-size:9.5px;color:#333;display:block}
.support-phone{font-size:17px;font-weight:400;color:#222;display:block;line-height:1}
.hero{position:absolute;left:171px;top:87px;width:859px;height:352px;background:linear-gradient(135deg,#d9dde3 0%,#aeb8c6 40%,#566277 75%,#2b3447 100%);box-shadow:0 2px 3px rgba(0,0,0,.25)}
.hero-caption{position:absolute;right:0;top:232px;display:flex;flex-direction:column;align-items:flex-end;gap:5px}
.hero-caption span{display:block;background:rgba(0,0,0,.78);color:#fff;font-size:22px;font-weight:300;padding:3px 7px;border:1px solid rgba(255,255,255,.25)}
.hero-caption span.second{margin-right:25px}
.hero-dots{position:absolute;left:13px;top:329px;display:flex;gap:5px}
.hero-dots i{width:11px;height:11px;border-radius:50%;background:#dde2f2}
.hero-dots i.on{background:var(--blue)}
.features{position:absolute;left:171px;top:471px;width:858px;display:flex;justify-content:space-between}
.feature{width:250px;position:relative;height:160px}
.feature-icon{width:60px;height:60px;border-radius:50%;background:#fff;border:1px solid #e6e6e6;box-shadow:inset 0 0 0 4px #f3f3f3;display:flex;align-items:center;justify-content:center}
.feature-title{position:absolute;left:75px;top:14px;font-size:16px;font-weight:400;color:var(--blue);line-height:20px}
.feature-text{margin-top:15px;font-size:10.5px;font-weight:300;color:var(--muted);line-height:15.5px}
.learn-more{position:absolute;right:0;top:146px;font-size:11px;color:#555;text-decoration:none}
.newsletter{position:absolute;left:171px;top:656px;width:858px;height:66px;background:#f7f7f7;border:1px solid var(--line);display:flex;align-items:center;padding:0 14px}
.newsletter h2{font-size:17px;font-weight:400;color:#666;width:207px}
.newsletter input{width:507px;height:40px;border:1px solid #e8e8e8;background:#fff;padding:0 10px;font-family:inherit;font-size:11px;font-style:italic;font-weight:300}
.newsletter input::placeholder{color:#aaa}
.btn-signup{margin-left:14px;width:102px;height:42px;border:1px solid var(--blue-dark);border-radius:3px;background:linear-gradient(var(--blue-light),var(--blue-dark));color:#fff;font-family:inherit;font-size:16px;font-weight:500;box-shadow:0 2px 2px rgba(0,0,0,.2)}
.blog-heading{position:absolute;left:172px;top:736px;font-size:19px;font-weight:400;color:#555}
.blog{position:absolute;left:171px;top:776px;width:858px;height:355px;background:var(--panel)}
.divider-v{position:absolute;left:429px;top:19px;width:1px;height:145px;background:var(--line)}
.divider-v.lower{top:196px;height:122px}
.divider-h{position:absolute;left:26px;top:172px;width:366px;height:1px;background:var(--line)}
.post{position:absolute;width:400px}
.post h3{font-size:14.5px;font-weight:300;color:#444;line-height:21px;width:270px}
.post p{margin-top:2px;font-size:10.5px;font-weight:300;color:var(--muted);line-height:15.5px;width:250px;margin-left:1px}
.post-thumb{position:absolute;left:321px;top:20px;width:95px;height:86px;border:1px solid #ddd;box-shadow:0 1px 2px rgba(0,0,0,.12)}
.btn-more{display:inline-block;margin-top:7px;width:56px;height:21px;line-height:19px;text-align:center;border-radius:11px;border:1px solid var(--blue-dark);background:linear-gradient(var(--blue-light),var(--blue-dark));color:#fff;font-size:11.5px;text-decoration:none}
.site-footer{position:absolute;left:0;top:1131px;width:1200px;height:50px;background:var(--footer);border-top:2px solid #222}
.footer-nav{position:absolute;left:176px;top:16px;display:flex;gap:12px}
.footer-nav a,.copyright{font-size:10px;color:#fff;text-decoration:none}
.copyright{position:absolute;right:174px;top:17px}
</style>
</head>
<body>
<header class="site-header">
  <div class="brand"><span class="brand-dot"></span><span class="brand-name">Brambleway Code Haulage</span></div>
  <nav class="main-nav">
    <a class="active" href="#">Home</a>
    <a href="#">About Us</a>
    <a href="#">Our Services</a>
    <a href="#">Contact Us</a>
  </nav>
  <div class="support">
    <svg width="32" height="34" viewBox="0 0 32 34" aria-hidden="true"><path d="M5 17a11 11 0 0 1 22 0" fill="none" stroke="#444" stroke-width="2.5"/><rect x="2" y="15" width="7" height="11" rx="3" fill="#333"/><rect x="23" y="15" width="7" height="11" rx="3" fill="#333"/><path d="M26 26q0 5-8 6" fill="none" stroke="#444" stroke-width="1.5"/><circle cx="17" cy="32" r="2" fill="#444"/></svg>
    <div class="support-text"><span class="support-label">24/7 Online Support Service</span><span class="support-phone">1-800-555-0142</span></div>
  </div>
</header>

<section class="hero" role="img" aria-label="Photo of a computer training room with rows of monitors and keyboards">
  <div class="hero-caption"><span>Brambleway Code Haulage</span><span class="second">Officially Launches!</span></div>
  <div class="hero-dots"><i></i><i class="on"></i><i></i><i></i></div>
</section>

<section class="features">
  <article class="feature">
    <div class="feature-icon"><svg width="34" height="34" viewBox="0 0 34 34" aria-hidden="true"><circle cx="17" cy="18" r="12" fill="#fff" stroke="#7083de" stroke-width="2.5"/><path d="M17 11v7l5 3" stroke="#7083de" stroke-width="2" fill="none"/><circle cx="7" cy="6" r="3.5" fill="#7083de"/><circle cx="27" cy="6" r="3.5" fill="#7083de"/></svg></div>
    <h3 class="feature-title">Portfolio<br>Management</h3>
    <p class="feature-text">Improve your packaging workflow by ensuring that the right information is collected avoiding additional testing or packaging and speeding up software requests.</p>
    <a class="learn-more" href="#">Learn More »</a>
  </article>
  <article class="feature">
    <div class="feature-icon"><svg width="40" height="40" viewBox="0 0 40 40" aria-hidden="true"><g fill="#7083de"><circle cx="20" cy="20" r="13"/><rect x="16" y="2" width="8" height="36" rx="2"/><rect x="2" y="16" width="36" height="8" rx="2"/><rect x="16" y="2" width="8" height="36" rx="2" transform="rotate(45 20 20)"/><rect x="16" y="2" width="8" height="36" rx="2" transform="rotate(-45 20 20)"/></g><circle cx="20" cy="20" r="6" fill="#fff"/></svg></div>
    <h3 class="feature-title">Build Management<br>And Automation</h3>
    <p class="feature-text">Reduce support costs and speed up desktop provisioning times by ensuring that you have a high quality automated desktop build image. We can assist you in creating your standard image.</p>
    <a class="learn-more" href="#">Learn More »</a>
  </article>
  <article class="feature">
    <div class="feature-icon"><svg width="40" height="40" viewBox="0 0 40 40" aria-hidden="true"><g stroke="#7083de" stroke-width="2"><path d="M20 3v6M8 8l4 4M32 8l-4 4M4 19h6M30 19h6"/></g><circle cx="20" cy="20" r="8" fill="#8e9ee8"/><rect x="16" y="27" width="8" height="7" rx="1" fill="#7083de"/></svg></div>
    <h3 class="feature-title">Training And<br>Consultancy</h3>
    <p class="feature-text">If you already have a team in place or would like your current processes to be reviewed, we're here to help.&nbsp; We can work with you to provide your team a bespoke training package on-site.</p>
    <a class="learn-more" href="#">Learn More »</a>
  </article>
</section>

<form class="newsletter">
  <h2>Sign Up For Newsletter</h2>
  <input type="email" placeholder="Enter your Email Address">
  <button class="btn-signup" type="button">SIGN UP</button>
</form>

<h2 class="blog-heading">From Our Blog</h2>

<section class="blog">
  <div class="divider-v"></div>
  <div class="divider-v lower"></div>
  <div class="divider-h"></div>

  <article class="post" style="left:26px;top:17px">
    <h3 style="width:310px">Isolating Wayfarer Browser Within Box-K</h3>
    <p>I recently came across a interesting scenario whilst sequencing Wayfarer Browser add-ons. My scenario was this: I had an Wayfarer Browser based application that required a specific version of Kettle.On the local PC image is a newer version of Kettle.</p>
    <a class="btn-more" href="#">More</a>
    <div class="post-thumb" role="img" aria-label="Flow diagram of incompatible applications in the enterprise" style="background:linear-gradient(#fff,#e9eefb 50%,#eef7e6)"></div>
  </article>

  <article class="post" style="left:464px;top:17px">
    <h3>What is a Package Accelerator?</h3>
    <p style="width:285px">Box-K 4.6 SP1 introduces a much hyped feature within the sequencer called 'package accelerators'. Dunmore describes these as:<br>"Dunmore Application Virtualization (Box-K) Package Accelerators.</p>
    <a class="btn-more" href="#">More</a>
    <div class="post-thumb" role="img" aria-label="Screenshot of the application virtualization sequencer start screen" style="left:319px;background:linear-gradient(#fff,#f1f1f6)"></div>
  </article>

  <article class="post" style="left:26px;top:194px">
    <h3>Box-K Command Line Interface</h3>
    <p>The Box-K CLI (command line interface) has been updated to support some of the new features in Box-K 4.6 SP1. This post will attempt to explain how to use the CLI including these new features. The Box-K CLI can be found.</p>
    <a class="btn-more" href="#">More</a>
    <div class="post-thumb" role="img" aria-label="Screenshot of a command line window with green text" style="background:linear-gradient(#0a1a0a,#143814 50%,#0a1a0a)"></div>
  </article>

  <article class="post" style="left:464px;top:194px">
    <h3>How To Run Local Applications Within an Box-K 5 Sequence</h3>
    <p style="width:280px">Those of us that are used to Box-K before version 5 may be used to using the Boxtray.exe with the /exe switch to run a command within the box-k sequence.</p>
    <a class="btn-more" href="#">More</a>
    <div class="post-thumb" role="img" aria-label="Diagram of two virtual environments sharing the operating system" style="left:319px;background:linear-gradient(#dfe3ea,#c9d3e6 50%,#dfe3ea)"></div>
  </article>
</section>

<footer class="site-footer">
  <nav class="footer-nav">
    <a href="#">Home</a><a href="#">About Us</a><a href="#">Our Services</a><a href="#">Contact Us</a>
  </nav>
  <p class="copyright">Copyrights © 2013 Brambleway Code Haulage. All rights Reserved</p>
</footer>
</body>
</html>
```